Individual Needs Design for Marketing Package

****IMPORTANT: Note that I have arranged an agreement with a specific designer to complete the design for the portfolio. Please do not submit any designs***

Goal
I recently resigned from my job in Canada, and I am moving down to Silicon Valley to pursue a career in the technology startup scene - initially doing technical sales. So my goal is to get a sales position with a startup tech company.

In order to land a sales position, I will be going to a startup conference in Silicon Valley which brings together over 2,000 startup technology companies. My goal is to meet the owners of some of these companies and demonstrate that I can be a valuable asset to their company. My challenge is that I have no existing relationships in Silicon Valley and limited experience in sales. So I have put together a portfolio of some of my most significant accomplishments over the past 6 years (see attached file). My hope is that this portfolio will convey that even though I have limited experience, I am passionate, driven, and loyal with a proven track record of achievement. After talking with them for 30 minutes and developing a rapport, I plan on giving this accomplishment portfolio (in addition to my resume) to CEOs of companies for which I could potentially work.

Message to Communicate
After someone reads my portfolio, I want them to view me as passionate, driven, and loyal with a proven track record of achievement. The design can communicate this message in a subtle way. The portfolio should also speak to my professionalism. It should certainly have some personality, but it should err on the side of professionalism.

Competitors
My competitors will be other people at the conference also looking to get sales positions with these startup companies. My main points of differentiation are that I am passionate, driven, and loyal with a proven track record of results. I would like this to be made a feature of the design.

Design Templates
I do not have any specific fonts or colours that I need you to use. The colours scheme and fonts selected should reinforce my key message.

Other Information
I do not own any specialized design software - only the basic microsoft word and powerpoint. However, I will need to be able to add new accomplishments to the portfolio and edit existing ones. Please let me know how this will be possible. I am not sure if it is possible to convert the final file into a file format that I can edit.

Notice that I have arranged the pages into sections. Feel free to rearrange the content within the sections, but please do not change the order of the sections

The size for the marketing package will be regular 8.5 x 11".
Updates

Target Market(s)

The people that will be reading my portfolio are owners of small technology companies in Silicon Valley. They are typically 28-35 years old, and highly logical thinkers. This means that the content is what is ultimately going to sell myself, but the design is what will make them want to read it. Therefore, the content should really stand out over the design.

Industry/Entity Type

Marketing

Requirements
Must have
• ****IMPORTANT: Note that I have arranged an agreement with a specific designer to complete the design for the portfolio. Please do not submit any designs***

I really view this portfolio as my personal marketing package, and that is where I need your expertise. I need you to take the content that I have in my portfolio and turn it into a personal marketing package. I need you to:

1. Design the cover page
2. Design the template for the content pages
3. Format the pictures and text to best fit the design of the pages**

** I would like the final design submission to include the pictures and text included in the attached file all fully formatted. However, when submitting the first iterations, please do not feel obligated to format the entire portfolio because I know that it can be time consuming. Just formatting the title page and the first content page should be enough to give me an idea of what the final portfolio will look like. Once we narrow it down to the final few designs, then we can start formatting the complete portfolio.

```html
<!DOCTYPE html>
<html lang="en">
<head>
<meta charset="utf-8">
<title>Leadership Spread – Daniel Mercer</title>
<link href="https://fonts.googleapis.com/css2?family=Lato:wght@300;400;700;900&display=swap" rel="stylesheet">
<style>
  :root {
    --backdrop: #454341;
    --paper: #ffffff;
    --ink: #2b2b2b;
    --map-land: #6a6770;
    --bar: #3a87c9;
    --bar-highlight: #0f5a88;
    --accent: #3a87c9;
  }
  * { margin: 0; padding: 0; box-sizing: border-box; }
  html, body {
    width: 1200px; height: 900px; overflow: hidden;
    background: var(--backdrop);
    font-family: "Lato", sans-serif;
    color: var(--ink);
  }
  .spread {
    position: absolute; left: 72px; top: 246px;
    width: 1056px; height: 408px;
    background: var(--paper);
  }
  .intro {
    position: absolute;
    font-weight: 300; font-size: 15.5px; line-height: 21px;
    text-align: right;
  }
  .intro--left { right: 566px; top: 56px; }
  .intro--right { right: 28px; top: 56px; }
  .world-map {
    position: absolute; left: 77px; top: 150px;
    width: 418px; height: 196px;
    background: linear-gradient(135deg, #6a6770 0%, #5d5a63 60%, #1f6a90 100%);
    border-radius: 4px;
  }
  .caption {
    position: absolute;
    font-weight: 900; font-size: 6.5px; letter-spacing: 0.1px;
  }
  .caption--map { right: 568px; top: 338px; }
  .caption--chart { left: 710px; top: 340px; }
  .exchange-chart { position: absolute; left: 0; top: 0; }
  .bar { fill: var(--bar); }
  .bar--current { fill: var(--bar-highlight); }
  .bar-value { fill: #fff; font: 900 5.5px "Lato", sans-serif; text-anchor: middle; }
  .bar-year { fill: var(--ink); font: 900 5px "Lato", sans-serif; text-anchor: middle; }
  .folio {
    position: absolute; top: 380px;
    font-size: 6.5px; letter-spacing: 0.4px; text-transform: uppercase;
    display: flex; align-items: center; gap: 6px;
  }
  .folio--left { left: 14px; }
  .folio--right { right: 28px; }
  .folio .section { color: var(--accent); }
  .folio-mark { width: 20px; height: 20px; background: var(--ink); display: inline-block; }
</style>
</head>
<body>
  <main class="spread">
    <p class="intro intro--left">The map shows the different countries<br>that we sent our interns to for work terms.</p>

    <div class="world-map" role="img" aria-label="World map highlighting the countries where Edmonton interns were placed in 2012, with arcs from Edmonton to each destination"></div>
    <p class="caption caption--map">NEXTERN Edmonton’s Outgoing Exchange Participants’ Locations in 2012</p>

    <p class="intro intro--right">The below chart shows the history of<br>NEXTERN Edmonton’s exchange results. We were<br>the fastest growing local committee in NEXTERN Canada.</p>

    <svg class="exchange-chart" width="1056" height="408" viewBox="0 0 1056 408" aria-label="Bar chart of total exchanges per year, 1998 to 2012">
      <g>
        <rect class="bar" x="630" y="295.5" width="13" height="27.5"/><text class="bar-value" x="636.5" y="305">7</text><text class="bar-year" x="636.5" y="331">1998</text>
        <rect class="bar" x="655.4" y="256.3" width="13" height="66.7"/><text class="bar-value" x="661.9" y="266">17</text><text class="bar-year" x="661.9" y="331">1999</text>
        <rect class="bar" x="680.8" y="260.3" width="13" height="62.7"/><text class="bar-value" x="687.3" y="270">16</text><text class="bar-year" x="687.3" y="331">2000</text>
        <rect class="bar" x="706.2" y="276" width="13" height="47"/><text class="bar-value" x="712.7" y="285.5">12</text><text class="bar-year" x="712.7" y="331">2001</text>
        <rect class="bar" x="731.6" y="264.2" width="13" height="58.8"/><text class="bar-value" x="738.1" y="274">15</text><text class="bar-year" x="738.1" y="331">2002</text>
        <rect class="bar" x="757" y="295.5" width="13" height="27.5"/><text class="bar-value" x="763.5" y="305">7</text><text class="bar-year" x="763.5" y="331">2003</text>
        <rect class="bar" x="782.4" y="276" width="13" height="47"/><text class="bar-value" x="788.9" y="285.5">12</text><text class="bar-year" x="788.9" y="331">2004</text>
        <rect class="bar" x="807.8" y="283.8" width="13" height="39.2"/><text class="bar-value" x="814.3" y="293">10</text><text class="bar-year" x="814.3" y="331">2005</text>
        <rect class="bar" x="833.2" y="264.2" width="13" height="58.8"/><text class="bar-value" x="839.7" y="274">15</text><text class="bar-year" x="839.7" y="331">2006</text>
        <rect class="bar" x="858.6" y="287.7" width="13" height="35.3"/><text class="bar-value" x="865.1" y="297">9</text><text class="bar-year" x="865.1" y="331">2007</text>
        <rect class="bar" x="884" y="283.8" width="13" height="39.2"/><text class="bar-value" x="890.5" y="293">10</text><text class="bar-year" x="890.5" y="331">2008</text>
        <rect class="bar" x="909.4" y="244.6" width="13" height="78.4"/><text class="bar-value" x="915.9" y="254">20</text><text class="bar-year" x="915.9" y="331">2009</text>
        <rect class="bar" x="934.8" y="236.8" width="13" height="86.2"/><text class="bar-value" x="941.3" y="246">22</text><text class="bar-year" x="941.3" y="331">2010</text>
        <rect class="bar" x="960.2" y="276" width="13" height="47"/><text class="bar-value" x="966.7" y="285.5">12</text><text class="bar-year" x="966.7" y="331">2011</text>
        <rect class="bar bar--current" x="985.6" y="170" width="13" height="153"/><text class="bar-value" x="992.1" y="179.5">39</text><text class="bar-year" x="992.1" y="331">2012</text>
      </g>
    </svg>
    <p class="caption caption--chart">Total Exchanges Each Year for NEXTERN Edmonton (Ultimate Performance Measure in NEXTERN)</p>

    <footer class="folio folio--left">P. 4 | Daniel Mercer | <span class="section">Leadership</span></footer>
    <footer class="folio folio--right"><span class="folio-mark" aria-hidden="true"></span>Daniel Mercer | <span class="section">Leadership</span> | P. 5</footer>
  </main>
</body>
</html>
```